Buchcover-Design für Coaching-Buch
Zielgruppe
22 Coaches (m/w/d) haben zusammen ein Buch geschrieben - mit ihren besten Tipps, Mut machenden Geschichten und Inspirationen. Herausgekommen ist 'Die stille Mentorin am Fensterbrett - 22 Schatzkisten lüften ihre Rätsel'. Zielgruppe sind vorwiegend Frauen, häufig mit spirituellem Hintergrund oder an Selbstentwicklung interessiert, sowie Menschen, die sich ermutigen lassen möchten und Menschen, die inspirierende Texte und Geschichten mögen. Die Themen sind ganz unterschiedlich, von Selbstliebe über die Wirkung von Farben, vom Überwinden von Krisen und Angst, Umgang mit Emotionen etc. pp. - ein ganzer Blumenstrauß an Themen.
Aufgabenstellung
Der Titel 'Die stille Mentorin am Fensterbrett' kam auf, weil wir die Vorstellung hatten, dass in dem Buch vielleicht abends im Bett gelesen wird und man dann ruhig schlafen kann.
Warum Füllhörner? Nun, jeder Coach hat viel zu geben. Zu jedem Text wird es ein Geschenk geben, das die Autor*innen online zur Verfügung stellen. Dies sind PDFs mit Tipps, Meditationen oder sogar eine kurze Gratis-Session. Es braucht also etwas auf dem Cover, das darauf hindeutet, vielleicht eine Plakette oder etwas Ähnliches, das 'Mit 22 Geschenken' besagt. Im Buchsatz wird dies durch einen Link (E-Book) und durch einen QR-Code (Print) umgesetzt.

```html
<!DOCTYPE html>
<html lang="de">
<head>
<meta charset="utf-8">
<title>Die stille Mentorin am Fensterbrett – Buchcover</title>
<link href="https://fonts.googleapis.com/css2?family=Lexend:wght@400&family=Lato:wght@400&display=swap" rel="stylesheet">
<style>
  :root {
    --stage: #e6e6e6;
    --paper: #ffffff;
    --ink: #3f5d59;
    --ink-soft: #5a7d78;
    --badge: #5f8985;
    --teal: #157a73;
    --green: #3ba36a;
    --yellow: #e6d43a;
    --orange: #e98a4f;
    --peach: #f2b48c;
    --rust: #a8432a;
  }
  * { box-sizing: border-box; margin: 0; padding: 0; }
  html, body {
    width: 1168px; height: 1200px; overflow: hidden;
    background: var(--stage);
  }
  .cover {
    position: absolute;
    left: 188px; top: 20px;
    width: 792px; height: 1160px;
    background: var(--paper);
    overflow: hidden;
  }
  .cover-art {
    position: absolute;
    left: 0; top: 0;
    width: 792px; height: 1160px;
  }
  .gift-badge {
    position: absolute;
    left: 700px; top: -20px;
    width: 62px; height: 300px;
    background: var(--badge);
    transform: rotate(5deg);
    transform-origin: top left;
    display: flex; align-items: center; justify-content: center;
  }
  .gift-badge span {
    display: block;
    transform: rotate(-90deg);
    white-space: nowrap;
    color: var(--paper);
    font-family: "Lato", sans-serif;
    font-size: 21px;
    letter-spacing: 0.04em;
    margin-top: 40px;
  }
  .title {
    position: absolute;
    right: 84px; top: 372px;
    text-align: right;
    color: var(--ink);
    font-family: "Lexend", sans-serif;
    font-weight: 400;
    font-size: 70px;
    line-height: 76px;
    letter-spacing: -0.01em;
  }
  .title span { display: block; }
  .subtitle {
    position: absolute;
    right: 84px; top: 850px;
    text-align: right;
    color: var(--ink-soft);
    font-family: "Lato", sans-serif;
    font-size: 21px;
    line-height: 28px;
    letter-spacing: 0.04em;
  }
  .subtitle span { display: block; }
</style>
</head>
<body>
  <main class="cover">
    <svg class="cover-art" viewBox="0 0 792 1160" role="img" aria-label="Platz für das aquarellartige Porträtmotiv in Petrol, Grün, Gelb, Orange und Rostrot">
      <defs>
        <linearGradient id="paint" x1="0" y1="0" x2="1" y2="0">
          <stop offset="0" stop-color="var(--teal)"/>
          <stop offset="0.22" stop-color="var(--green)"/>
          <stop offset="0.34" stop-color="var(--yellow)"/>
          <stop offset="0.52" stop-color="var(--orange)"/>
          <stop offset="0.8" stop-color="var(--peach)"/>
          <stop offset="1" stop-color="var(--peach)" stop-opacity="0"/>
        </linearGradient>
        <linearGradient id="fade" x1="0" y1="0" x2="0" y2="1">
          <stop offset="0" stop-color="#fff" stop-opacity="0"/>
          <stop offset="0.15" stop-color="#fff" stop-opacity="1"/>
          <stop offset="1" stop-color="#fff" stop-opacity="1"/>
        </linearGradient>
        <mask id="art-mask">
          <rect x="0" y="240" width="480" height="920" fill="url(#fade)"/>
        </mask>
      </defs>
      <rect x="0" y="240" width="480" height="920" fill="url(#paint)" mask="url(#art-mask)"/>
    </svg>

    <div class="gift-badge"><span>MIT 22 GESCHENKEN</span></div>

    <h1 class="title">
      <span>Die</span>
      <span>stille</span>
      <span>Mentorin</span>
      <span>am</span>
      <span>Fenster-</span>
      <span>brett</span>
    </h1>

    <p class="subtitle">
      <span>22 SCHATZKISTEN</span>
      <span>LÜFTEN IHRE</span>
      <span>RÄTSEL.</span>
    </p>
  </main>
</body>
</html>
```